Bellmoor Commercial Finance Information Brochure

This brochure will be sent out to clients via A4 PDF on an email to showcase what our company has to offer. We are a commercial finance brokerage, that specialises in property finance. We would like to see designs following our colour scheme. The final design should demonstrate our professionalism and reliability.
I have attached our logo and also a few bullet points on our information and what we can offer. These can be slightly reworded for conciseness. Or leave the text sections as filler and I can fill these in.
I have also attached an overview of our colour scheme and design styling for your consideration.
Target Market(s)
Property Developers
Industry/Entity Type
Financial Services

```html
<!DOCTYPE html>
<html lang="en">
<head>
<meta charset="utf-8">
<title>Bellmoor Commercial Finance – Information Brochure</title>
<link rel="stylesheet" href="https://fonts.googleapis.com/css2?family=Open+Sans:wght@400;700&display=swap">
<style>
  :root {
    --bg: #d9d9de;
    --paper: #f7f7f7;
    --brand-blue: #1740a8;
    --brand-green: #1f8a3b;
    --ink: #2b2b2b;
    --photo-green-a: #4f7a3a;
    --photo-green-b: #a9b98a;
    --photo-teal-a: #3f7d89;
    --photo-teal-b: #5f97a2;
  }
  * { box-sizing: border-box; margin: 0; padding: 0; }
  html, body { width: 1200px; height: 840px; overflow: hidden; }
  body {
    background: var(--bg);
    font-family: "Open Sans", sans-serif;
    color: var(--ink);
    display: flex;
    justify-content: center;
    align-items: center;
  }
  .spread { display: flex; width: 1188px; height: 840px; }
  .page {
    position: relative;
    width: 594px;
    height: 840px;
    background: var(--paper);
    overflow: hidden;
  }
  .page--left { border-right: 1px solid #e2e2e2; }
  .photo { width: 100%; }
  .photo--growth {
    height: 290px;
    background:
      linear-gradient(180deg, transparent 60%, rgba(180,138,92,0.55) 100%),
      radial-gradient(circle at 70% 30%, var(--photo-green-b), var(--photo-green-a) 70%);
  }
  .photo--keys {
    height: 230px;
    background:
      radial-gradient(ellipse at 60% 55%, #e9e6df 0 18%, transparent 19%),
      linear-gradient(160deg, var(--photo-teal-b), var(--photo-teal-a));
  }
  .copy { position: relative; z-index: 1; padding: 24px 46px 0; font-size: 11.5px; line-height: 1.5; }
  .copy p { margin-bottom: 10px; }
  .lead {
    color: var(--brand-blue);
    font-weight: 700;
    font-size: 13px;
    line-height: 1.4;
    margin-bottom: 10px;
  }
  .callout { color: var(--brand-green); font-weight: 700; font-size: 12.5px; }
  .callout--blue { color: var(--brand-blue); }
  .swoosh { position: absolute; left: 0; bottom: 0; width: 594px; }
</style>
</head>
<body>
  <main class="spread">
    <section class="page page--left">
      <div class="photo photo--growth" role="img" aria-label="Photo of a small wooden house beside growing stacks of coins with seedlings, against blurred greenery"></div>
      <div class="copy">
        <h2 class="lead">As former lenders and developers ourselves, we intimately understand the inefficiencies that plague deals in the market today.</h2>
        <p>We’ve experienced the frustration of tight time limits on deals and the exasperating feeling of brokers wasting precious time collecting information. It’s enough to drive developers and lenders insane!</p>
        <p>That’s why we founded Bellmoor Finance – to be the efficient and reliable link that connects developers and lenders.</p>
        <p>We’ve streamlined our processes to eliminate unnecessary hurdles, enabling clear and swift communication between all parties involved.</p>
        <p class="callout">No more wasted time. No more unnecessary stress.</p>
        <p>With our background in the asset management industry, we have cultivated a black book of fund managers, institutions, UHNWI and private equity lenders that we can call on for non-traditional lending.</p>
      </div>
      <svg class="swoosh" height="190" viewBox="0 0 594 190" aria-hidden="true">
        <path d="M0 20 C 180 70, 400 130, 594 190 L 0 190 Z" fill="var(--brand-green)"/>
        <path d="M0 30 C 180 80, 390 135, 566 190 L 0 190 Z" fill="var(--paper)"/>
        <path d="M0 42 C 170 92, 370 142, 530 190 L 0 190 Z" fill="var(--brand-blue)"/>
      </svg>
    </section>

    <section class="page page--right">
      <div class="photo photo--keys" role="img" aria-label="Photo of house keys and a wooden model house resting on a document on a teal surface"></div>
      <div class="copy">
        <p>With our expertise and industry insights, we’ve developed a unique approach that simplifies the financing journey. From the initial consultation to the final funding,</p>
        <p class="callout callout--blue">we’re here to guide you every step of the way. Our goal?</p>
        <p>To make commercial financing a smooth and enjoyable experience for you. We are well-versed in the questions lenders will ask, allowing us to get ahead of the curve and request all the necessary information from you on day one. This approach provides you with a distinct advantage, as it eliminates</p>
        <p>the need to allocate hours each day to answering questions and fulfilling requests from brokers. By entrusting us with this responsibility, you can focus on your core tasks and leave the financing aspect to us, making the process less stressful for you.</p>
        <p>Bellmoor Finance was created to satisfy a need in the market that has been far too overlooked. Efficiency. Efficiency is at the heart of our operations, and we pride ourselves on our ability to secure the best financing options swiftly and effectively for our clients. By employing cutting-edge technology and streamlining our internal processes, we have cultivated a seamless and time-saving approach to finance brokering. Having been a developer, we understand the stresses and headaches associated with building, let alone all the paperwork and emails backwards and forwards between yourself and brokers to attain the necessary financing.</p>
      </div>
      <svg class="swoosh" height="130" viewBox="0 0 594 130" aria-hidden="true">
        <path d="M0 10 C 200 50, 420 62, 594 56 L 594 130 L 0 130 Z" fill="var(--brand-green)"/>
        <path d="M0 20 C 200 62, 420 74, 594 70 L 594 130 L 0 130 Z" fill="var(--paper)"/>
        <path d="M0 28 C 200 72, 420 84, 594 82 L 594 130 L 0 130 Z" fill="var(--brand-blue)"/>
      </svg>
    </section>
  </main>
</body>
</html>
```